Ad Banner for knowledge management portal - Promote Knowledge Submission

This banner is used in knowledge management web site.

1. Banner size: 940x380
2. Business background: Provides maintenance, design and engineering, construction, machinery operation, material procurement and production management services for petrochemical and refinery business
3. We would like to see designs that
- Promote the benefits of sharing "Lesson Learned".
- Use the keyword "I will do it better if I have to do it again"
- Promote employees to submit "Lesson Learned". It is a lesson learned from work, submitted using a predefined form template.
- Promote a campaign that will give out souvenir for all employees who submit "Lesson Learned"
- Has the message "Click here to learn more about Lesson Learned"

Requirements
Must have
• Must have a picture of technician examining machine or equipments (using cartoon character)
Should not have
• Should not include picture of real people in the design

```html
<!DOCTYPE html>
<html lang="en">
<head>
<meta charset="utf-8">
<title>Lesson Learned – Knowledge Sharing Banner</title>
<link href="https://fonts.googleapis.com/css2?family=Arimo:wght@400;700&family=Roboto+Condensed:wght@400;700&display=swap" rel="stylesheet">
<style>
  :root {
    --sky-top: #b7cada;
    --sky-mid: #dfe8ef;
    --sky-haze: #f2f5f7;
    --grass-light: #a6d25c;
    --grass-dark: #6aa834;
    --plant-tone: #a3b3c1;
    --figure-tone: #c3d0dc;
    --brand-blue: #2a78c2;
    --ink-dark: #0f1d2b;
    --ink-body: #1b1b1b;
  }
  html, body {
    margin: 0;
    padding: 0;
    overflow: hidden;
    background: #ffffff;
  }
  .banner {
    position: relative;
    width: 1200px;
    height: 485px;
    overflow: hidden;
    font-family: "Arimo", Arial, sans-serif;
  }
  .scene-backdrop {
    position: absolute;
    inset: 0;
    background: linear-gradient(180deg,
      var(--sky-top) 0%,
      var(--sky-mid) 40%,
      var(--sky-haze) 72%,
      var(--grass-light) 78%,
      var(--grass-dark) 100%);
  }
  .refinery-area {
    position: absolute;
    left: 880px;
    top: 190px;
    width: 240px;
    height: 190px;
    background: linear-gradient(180deg, rgba(163,179,193,0) 0%, rgba(163,179,193,0.6) 45%, rgba(140,158,175,0.8) 100%);
  }
  .mascot-area {
    position: absolute;
    left: 945px;
    top: 70px;
    width: 198px;
    height: 396px;
    background: linear-gradient(180deg, var(--figure-tone) 0%, #b6c5d4 55%, #2f343a 100%);
    border-radius: 80px 80px 20px 20px;
    opacity: 0.85;
  }
  .headline {
    position: absolute;
    left: 42px;
    top: 30px;
    margin: 0;
    font-family: "Roboto Condensed", "Arial Narrow", sans-serif;
    font-weight: 700;
    font-size: 118px;
    line-height: 1;
    color: var(--ink-dark);
    white-space: nowrap;
  }
  .headline .accent { color: var(--brand-blue); }
  .tagline {
    position: absolute;
    left: 45px;
    top: 150px;
    margin: 0;
    font-weight: 400;
    font-size: 45px;
    line-height: 1.1;
    letter-spacing: -0.5px;
    color: var(--ink-dark);
    white-space: nowrap;
  }
  .tagline .accent { color: var(--brand-blue); }
  .services {
    position: absolute;
    left: 45px;
    top: 244px;
    width: 820px;
    margin: 0;
    font-family: "Roboto Condensed", "Arial Narrow", sans-serif;
    font-size: 17.5px;
    line-height: 35px;
    color: var(--ink-body);
  }
  .cta {
    position: absolute;
    left: 51px;
    top: 428px;
    margin: 0;
    font-size: 21px;
    color: var(--ink-body);
    text-decoration: none;
    white-space: nowrap;
  }
  .cta strong { font-weight: 700; color: var(--ink-dark); }
</style>
</head>
<body>
  <div class="banner">
    <div class="scene-backdrop" role="img" aria-label="Engineering blueprints fading into a pale sky above a green meadow"></div>
    <div class="refinery-area" role="img" aria-label="Petrochemical refinery towers on the horizon"></div>
    <div class="mascot-area" role="img" aria-label="Cartoon technician in shirt and tie pointing toward the message"></div>

    <h1 class="headline"><span class="accent">Lesson</span> Learned</h1>
    <p class="tagline">I will do it <span class="accent">better</span> if I have to do it <span class="accent">again....</span></p>
    <p class="services">Provides maintenance, design and engineering, construction, machinery operation, material procurement and production management services for petrochemical and refinery business</p>
    <a class="cta" href="#">Click here to learn more about <strong>Lesson Learned</strong></a>
  </div>
</body>
</html>
```